TunedLobe need a flyer designed for musician hearing protection products

TunedLobe is a company who specializes in custom hearing protection for the general public and musicians. In addition we offer in-ear monitors for musicians. We need a flyer designed that we can distribute in concert halls, recording studios, musicians, showing the products that we offer, services provided. THe flyer needs to be catchy to get peoples attention and informative at the same time. Currently we are using Chatterbox as the web page (www.tunedlobe-example.com). The manufacturers that we work with are: www.qrvmolds-example.com www.harbinfield-example.com www.plovimetrics-example.com
I am sorry I forgot to add that the flyer will be double sided. On the other side I would like to have a noise exposure chart showing the damage that you would get from different noise exposed situations. There are some charts on the internet but obviously I would like this one to be on a creative side, and contact information.
This will give you an idea of the products that we offer to the public.
Musicians, sounds engineers, general public attending concerts
Internet

```html
<!DOCTYPE html>
<html lang="en">
<head>
<meta charset="UTF-8">
<title>TunedLobe – Custom Hearing Protection Flyer</title>
<link rel="stylesheet" href="https://fonts.googleapis.com/css2?family=Open+Sans:wght@300;400;600&display=swap">
<style>
  :root {
    --brand-blue: #2e6cb4;
    --brand-blue-deep: #1d4a86;
    --brand-blue-dark: #163a6c;
    --brand-blue-light: #6b9fd6;
    --stage-wood: #4f86c6;
    --panel-black: #1b1b1b;
    --accent-cyan: #3bb4ea;
    --text-white: #ffffff;
    --text-body: #4a4a4a;
    --text-dark: #222222;
    --page-bg: #ffffff;
  }
  * { box-sizing: border-box; margin: 0; padding: 0; }
  html, body { width: 848px; height: 1200px; overflow: hidden; background: var(--page-bg); }
  body { font-family: "Open Sans", Arial, sans-serif; }

  .flyer { position: relative; width: 848px; height: 1200px; background: var(--page-bg); }

  .hero-photo {
    position: absolute; left: 0; top: 0; width: 848px; height: 827px;
    background:
      radial-gradient(ellipse 260px 180px at 560px 360px, rgba(150,190,235,0.45) 0%, transparent 70%),
      radial-gradient(ellipse 420px 260px at 250px 380px, rgba(20,50,100,0.55) 0%, transparent 75%),
      radial-gradient(ellipse 300px 200px at 160px 120px, rgba(120,165,220,0.35) 0%, transparent 70%),
      linear-gradient(165deg, transparent 52%, var(--stage-wood) 62%, var(--brand-blue-light) 78%, var(--stage-wood) 100%),
      linear-gradient(180deg, var(--brand-blue-dark) 0%, var(--brand-blue-deep) 30%, var(--brand-blue) 60%, var(--brand-blue) 100%);
    border-bottom: 2px solid var(--brand-blue-deep);
  }

  .logo-panel {
    position: absolute; left: 449px; top: 0; width: 399px; height: 295px;
    background: var(--panel-black);
  }
  .logo-mark {
    position: absolute; left: 36px; top: 105px;
    display: flex; align-items: center; gap: 16px;
  }
  .logo-name {
    font-weight: 600; font-size: 30px; color: var(--text-white); letter-spacing: 0.2px;
  }
  .logo-dot {
    width: 22px; height: 22px; border-radius: 50%; background: var(--accent-cyan);
  }

  .headline {
    position: absolute; right: 20px; top: 400px; text-align: right; color: var(--text-white);
  }
  .headline-main {
    font-weight: 300; font-size: 87px; line-height: 1; letter-spacing: 1px;
  }
  .headline-sub {
    font-weight: 300; font-size: 28.5px; line-height: 1; margin-top: 2px;
  }

  .provides {
    position: absolute; right: 21px; top: 610px; text-align: right; color: var(--text-white);
  }
  .provides-title { font-weight: 300; font-size: 53px; line-height: 1; margin-bottom: 26px; }
  .provides-list { list-style: none; }
  .provides-list li {
    font-weight: 300; font-size: 24px; line-height: 33px;
    display: flex; justify-content: flex-end; align-items: center;
  }
  .provides-list li::after {
    content: ""; width: 9px; height: 9px; border-radius: 50%;
    background: var(--text-white); margin-left: 19px; margin-right: 4px;
  }

  .intro-text {
    position: absolute; left: 76px; top: 862px; width: 708px;
    font-size: 15.7px; line-height: 26px; color: var(--text-body);
  }

  .site-url {
    position: absolute; left: 0; right: 0; top: 1164px; text-align: center;
    font-size: 15px; color: var(--text-dark);
  }
</style>
</head>
<body>
  <main class="flyer">
    <div class="hero-photo" role="img" aria-label="Orchestra rehearsing on a concert hall stage with a conductor, tinted blue"></div>

    <div class="logo-panel">
      <div class="logo-mark">
        <span class="logo-name">Marek Talvin</span>
        <span class="logo-dot"></span>
      </div>
    </div>

    <header class="headline">
      <h1 class="headline-main">SPECIALIZES IN</h1>
      <p class="headline-sub">CUSTOM HEARING PROTECTION</p>
    </header>

    <section class="provides">
      <h2 class="provides-title">PROVIDES</h2>
      <ul class="provides-list">
        <li>Ear Molds</li>
        <li>Hearing Protection</li>
        <li>In-ear Monitors</li>
      </ul>
    </section>

    <p class="intro-text">TunedLobe makes custom hearing protection for musicians, sound engineers and everyone who loves live music. Every mold is shaped to your own ear, so it seals well, stays comfortable through a full show and keeps the sound clear while it protects your hearing.</p>

    <footer class="site-url">www.tunedlobe-example.com</footer>
  </main>
</body>
</html>
```